Upscale Children's Boutique Needs a PSD Web Design

We need a PSD web design for an online children's boutique called 'Mavoret'. We specialize in special occasion wear for infants. Our apparel products are typically selected for christening & baptisms, birthdays, holidays and weddings. We would like to see designs that compliment our existing logo and business card. The final design should communicate a sense of luxury, but also be fun and oriented towards children.
Our current website is www.mavoret.com. Note: Not all products are loaded.
Changes to the color scheme, fonts, background and graphics are welcome. And while we like the layout of my current TrellaCart theme (Seashore), we do expect that SMALL modifications will be needed to make it ours. For example, we would like the cart to be placed more visibly. I have a designer that can code the changes you come up with so feel free to suggest what you feel is best.
We look forward to your designs. Good luck!
Websites we like:
https://www.shopwrenfig.com/ (The layout of this site is nice to me)
http://www.elsiesattic.com/
http://www.quietmeadowherbals.com/
Updates
This contest is for PSD design only. No Trellacart development or coding is required.
Target Market(s)
Our typical customer is female age 20-45 shopping for her own child or for a gift.
Industry/Entity Type
Boutique
Requirements
Must have
- PSD Design
- These 5 items listed below are things we’d like:
- (1) General styling (color scheme, fonts, background, graphics, etc.) & layout
- • ONLY the logo colors are set … feel free to add colors that compliment it
- • Prefer narrow (or single line) footer
- • We think the main banner/image is too large
- (2) Create main banner/image (current template uses 970px wide)
- (3) AT LEAST Three (3) Marketing banners (current template uses 433 x 225):
- • Our Hottest Products
- • Our Newest Arrivals
- • Newsletter sign-up
- (4) Border to enclose admin links (My account, Gift Certificates, Create an Account)
- (5) New badges / icon / images
- • Shopping Cart --> Bag or cart image should stand out; try to place above search bar (you’ll have to lower the search bar to do this)
- • Sale Badge --> anything goes. Could be a badge or a sash. Might also be nice to have these for the bestsellers as well.
- • Star Icons for product reviews (optional) --> Keep the stars just have them be more stylized
Nice to have
- We like pages that have a background and think one might look good on our site if not too busy.
Should not have
- We do not like extremely dark backgrounds for web pages.

```html
<!DOCTYPE html>
<html lang="en">
<head>
<meta charset="utf-8">
<title>Mavoret Childrenswear</title>
<link href="https://fonts.googleapis.com/css2?family=Roboto:wght@300;400;500;700&display=swap" rel="stylesheet">
<style>
:root{
  --sky:#bfeef0;
  --sky-deep:#a3e3e7;
  --teal:#5fc3c6;
  --teal-mid:#4aa9ab;
  --teal-dark:#2f7d80;
  --teal-ink:#1f7478;
  --peach:#f2a887;
  --peach-btn:#eea07c;
  --peach-foot:#eda58a;
  --ink:#333;
  --grey:#cfd3d3;
  --white:#fff;
}
*{margin:0;padding:0;box-sizing:border-box}
html,body{width:891px;height:1200px;overflow:hidden}
body{position:relative;font-family:'Roboto',sans-serif;color:var(--ink);
  background:linear-gradient(180deg,var(--sky) 0%,var(--sky-deep) 100%)}
.abs{position:absolute}
.admin-link{top:8px;height:21px;border:1px solid #5a6e70;background:rgba(255,255,255,.35);font-size:10px;line-height:19px;text-align:center;color:#333}
.cart-badge{left:678px;top:5px;width:27px;height:27px;border-radius:50%;background:var(--peach);border:2px solid #fff;box-shadow:0 0 0 1px #c98a6e}
.cart-text{left:713px;top:13px;font-size:10px;font-weight:500;color:#222}
.page{left:45px;top:36px;width:801px;height:996px;background:var(--white);border-radius:10px;box-shadow:0 0 6px rgba(0,0,0,.12)}
.brand-dot{left:56px;top:62px;width:22px;height:22px;border-radius:50%;background:var(--teal)}
.brand-tag{left:96px;top:55px;font-size:5.5px;color:var(--teal-ink)}
.brand-name{left:95px;top:62px;font-size:32px;font-weight:300;color:var(--teal-ink);letter-spacing:1px}
.brand-sub{left:96px;top:102px;font-size:7.5px;letter-spacing:1.5px;color:var(--teal-ink)}
.call{left:534px;top:55px;font-size:9.5px;color:#222;display:flex;align-items:center;gap:5px}
.call b{font-weight:500}.call span{color:var(--teal-ink)}
.search{left:670px;top:48px;width:166px;height:25px;border:1px solid var(--grey);font-size:9px;font-style:italic;color:#999;padding:6px 8px}
.nav{left:322px;top:83px;width:514px;height:31px;background:var(--teal);display:flex}
.nav a{color:#fff;font-size:9.5px;line-height:31px;padding:0 12px;text-decoration:none}
.nav a.on{background:var(--peach);width:55px;padding:0;text-align:center}
.hero-frame{left:54px;top:118px;width:783px;height:281px;border:1px solid #ddd;background:#fff}
.hero-img{left:61px;top:124px;width:769px;height:269px;
  background:
    radial-gradient(ellipse 150px 130px at 560px 95px,rgba(250,240,242,.95) 0%,rgba(240,222,224,.7) 45%,rgba(240,222,224,0) 100%),
    radial-gradient(ellipse 190px 120px at 570px 230px,rgba(247,232,236,.95) 0%,rgba(235,210,216,.6) 50%,rgba(235,210,216,0) 100%),
    linear-gradient(180deg,rgba(0,0,0,0) 0%,rgba(0,0,0,0) 82%,#dba9b4 88%,#cf96a3 100%),
    linear-gradient(90deg,#a99d9c 0%,#bdb0ac 35%,#cdbfba 60%,#c2b2ad 85%,#b3a4a1 100%)}
.hero-h1{left:89px;top:182px;font-size:32px;font-weight:700;color:#fff;letter-spacing:.5px}
.hero-h2{left:89px;top:222px;font-size:21px;font-weight:700;color:var(--teal-ink);line-height:28px}
.btn{background:var(--peach-btn);color:#fff;text-align:center;font-weight:500}
.hero-btn{left:89px;top:280px;width:101px;height:31px;font-size:11.5px;line-height:31px;font-weight:700}
.dot{top:364px;width:10px;height:10px;background:#222}
.hero-shadow{left:100px;top:399px;width:690px;height:16px;background:radial-gradient(ellipse at top,rgba(0,0,0,.12),transparent 70%)}
.promo{top:430px;width:245px;height:154px;border:2px solid var(--teal);overflow:hidden}
.promo .art{position:absolute;inset:0}
.promo h3{position:absolute;left:13px;top:12px;font-size:17px;font-weight:400;color:#222;line-height:20px}
.promo h3 b{display:block;font-size:22px;font-weight:700;letter-spacing:.5px}
.promo .btn{position:absolute;left:13px;bottom:13px;width:84px;height:26px;font-size:9px;line-height:26px;font-weight:400}
.email{position:absolute;left:17px;top:69px;width:211px;height:30px;background:#fff;font-size:9px;font-style:italic;color:#777;padding:10px 10px}
.rule{left:55px;top:609px;width:781px;height:3px;background:#e6e6e6}
.feat-title{left:55px;top:629px;font-size:17.5px;font-weight:400;color:#222;letter-spacing:.3px}
.card{top:663px;width:179px;height:249px;border:2px solid #e4e4e4;background:#fff}
.card .pic{position:absolute;left:22px;top:14px;width:131px;height:122px;border-radius:4px;
  background:linear-gradient(160deg,#fbfbfb 0%,#eef0f1 55%,#e2e5e6 100%)}
.card .qv{position:absolute;left:54px;top:88px;width:68px;height:24px;background:var(--teal);color:#fff;font-size:8px;line-height:24px;text-align:center}
.card .name{position:absolute;left:14px;top:144px;font-size:10px;line-height:14.5px;color:#222}
.card .stars{position:absolute;left:14px;top:180px}
.card .price{position:absolute;left:14px;top:210px;font-size:14px;color:#222}
.card .btn{position:absolute;left:79px;top:206px;width:83px;height:25px;font-size:9px;line-height:25px;font-weight:400}
.sale{left:55px;top:928px;width:781px;height:89px;overflow:hidden;
  background:
    radial-gradient(ellipse 150px 60px at 520px 40px,rgba(245,247,248,.9),rgba(245,247,248,0)),
    radial-gradient(ellipse 140px 50px at 700px 80px,#6f8fb8,rgba(111,143,184,0)),
    linear-gradient(90deg,#7f8b90 0%,#a7b2b6 45%,#d9dfe1 70%,#8796a4 100%)}
.sale-band{left:0;top:0;width:781px;height:89px}
.sale h2{position:absolute;left:20px;top:14px;font-size:30px;font-weight:700;color:#fff}
.sale p{position:absolute;left:20px;top:52px;font-size:19px;font-weight:500;color:var(--peach)}
.sale .btn{position:absolute;left:259px;top:31px;width:101px;height:26px;background:var(--teal-mid);font-size:11px;line-height:26px;font-weight:400}
.perks{left:0;top:1048px;width:891px;height:66px;display:flex;background:var(--teal-mid)}
.perk{display:flex;align-items:center;color:#fff}
.perk h4{font-size:19px;font-weight:400;letter-spacing:.5px;line-height:20px}
.perk small{display:block;font-size:11px;font-weight:500;color:#12393b;letter-spacing:.4px}
.footer{left:0;top:1114px;width:891px;height:86px;background:var(--peach-foot)}
.copy{left:55px;top:1140px;font-size:8.5px;color:#fff;line-height:16px}
.social{left:613px;top:1138px;display:flex;align-items:center;gap:3px;font-size:10px;color:#fff}
.social .lbl{margin-right:6px}
.social i{width:24px;height:24px;border-radius:50%;display:block}
</style>
</head>
<body>
<div class="abs admin-link" style="left:385px;width:72px">My Account</div>
<div class="abs admin-link" style="left:462px;width:89px">Gift Certificates</div>
<div class="abs admin-link" style="left:558px;width:100px">Create an Account</div>
<div class="abs cart-badge">
  <svg width="23" height="23" viewBox="0 0 23 23"><path d="M6 9h11l-1.5 6h-8z" fill="#2b5a5c"/><path d="M8 9l3.5-4 3.5 4" stroke="#2b5a5c" stroke-width="1.2" fill="none"/></svg>
</div>
<div class="abs cart-text">SHOPPING CART: $0.00 &nbsp;(0)</div>

<div class="abs page"></div>

<div class="abs brand-dot"></div>
<div class="abs brand-tag">Special Occasion Bibs &amp; Pieces</div>
<div class="abs brand-name">Mavoret</div>
<div class="abs brand-sub">CHILDRENSWEAR</div>

<div class="abs call">
  <svg width="11" height="11" viewBox="0 0 11 11"><rect width="11" height="11" rx="2" fill="var(--teal-ink)"/><path d="M3 2.5c0 3 2.5 5.5 5.5 5.5l.5-1.5-1.8-.8-.8.8c-1-.4-1.8-1.2-2.2-2.2l.8-.8L4.2 1.7z" fill="#fff"/></svg>
  <b>CALL:</b> <span>(555) 014-2278</span>
</div>
<div class="abs search">Search...
  <svg style="position:absolute;right:7px;top:6px" width="13" height="13" viewBox="0 0 13 13"><circle cx="5" cy="5" r="3.8" stroke="var(--teal-ink)" stroke-width="1.6" fill="none"/><path d="M8 8l4 4" stroke="var(--teal-ink)" stroke-width="2"/></svg>
</div>
<nav class="abs nav">
  <a class="on">HOME</a><a>CHRISTENING &amp; BAPTISMS</a><a>BIRTHDAYS</a><a>HOLIDAYS</a><a>WEDDINGS</a><a>CONTACT US</a>
</nav>

<div class="abs hero-frame"></div>
<div class="abs hero-img" role="img" aria-label="Baby in a soft white knit hat and white top on a pink blanket"></div>
<div class="abs hero-h1">ALIQUAM MOLESTIE</div>
<div class="abs hero-h2">DUIS ALIQUAM NIBH A<br>DUI IACULIS..</div>
<div class="abs btn hero-btn">SHOP NOW</div>
<div class="abs dot" style="left:89px;background:#fff"></div>
<div class="abs dot" style="left:105px"></div>
<div class="abs dot" style="left:121px"></div>
<div class="abs dot" style="left:137px"></div>
<div class="abs hero-shadow"></div>

<section class="abs promo" style="left:56px">
  <div class="art" role="img" aria-label="Stack of folded pink and lilac baby clothes" style="background:radial-gradient(ellipse 110px 80px at 190px 100px,#f6d8f0 0%,#eec9ea 45%,rgba(238,201,234,0) 100%),radial-gradient(ellipse 60px 30px at 170px 8px,#f07cae,rgba(240,124,174,0)),linear-gradient(100deg,#d6d7f1 0%,#ddd6f0 55%,#e9d3ee 100%)"></div>
  <h3>Our Hottest<b>PRODUCTS</b></h3>
  <div class="btn">SHOP NOW</div>
</section>
<section class="abs promo" style="left:323px;border-color:var(--teal-dark)">
  <div class="art" role="img" aria-label="Stack of folded colourful baby clothes with a pacifier" style="background:radial-gradient(ellipse 80px 30px at 185px 50px,#e0676a,rgba(224,103,106,0)),radial-gradient(ellipse 90px 35px at 190px 130px,#3e74b8,rgba(62,116,184,0)),radial-gradient(ellipse 80px 40px at 190px 90px,#f3f1ec,rgba(243,241,236,0)),linear-gradient(100deg,#6ccfd0 0%,#7fd3d6 55%,#6fc6c9 100%)"></div>
  <h3>Our Newest<b>ARRIVALS</b></h3>
  <div class="btn">SHOP NOW</div>
</section>
<section class="abs promo" style="left:591px">
  <div class="art" role="img" aria-label="Turquoise background with a pacifier and flower" style="background:radial-gradient(circle 26px at 206px 22px,#a5e3e6,rgba(165,227,230,0)),radial-gradient(ellipse 34px 26px at 26px 118px,#5aa9d6,rgba(90,169,214,0)),linear-gradient(120deg,#7fd5d6,#6fcdd0)"></div>
  <h3>Newsletter<b>SIGN-UP</b></h3>
  <div class="email">Enter Email Address</div>
  <div class="btn" style="left:auto;right:17px">SUBSCRIBE</div>
</section>

<div class="abs rule"></div>
<div class="abs feat-title">FEATURED PRODUCTS</div>
<svg class="abs" style="left:806px;top:631px" width="34" height="14" viewBox="0 0 34 14"><path d="M8 1L2 7l6 6M26 1l6 6-6 6" stroke="#333" stroke-width="1.4" fill="none"/></svg>

<svg width="0" height="0" style="position:absolute"><defs>
<symbol id="star" viewBox="0 0 12 12"><path d="M6 .6l1.6 3.5 3.8.4-2.9 2.6.8 3.8L6 9 2.7 10.9l.8-3.8L.6 4.5l3.8-.4z"/></symbol></defs></svg>

<article class="abs card" style="left:56px">
  <div class="pic" role="img" aria-label="White organza christening booties"></div>
  <div class="qv">QUICK VIEW</div>
  <div class="name">Organza Trim Christening<br>Bootie WHITE</div>
  <svg class="stars" width="72" height="12"><g fill="#f6c20c"><use href="#star" x="0" width="12" height="12"/><use href="#star" x="15" width="12" height="12"/><use href="#star" x="30" width="12" height="12"/><use href="#star" x="45" width="12" height="12"/></g><use href="#star" x="60" width="12" height="12" fill="none" stroke="#f6c20c" stroke-width=".9"/></svg>
  <div class="price">$14.00</div><div class="btn">ADD TO CART</div>
</article>
<article class="abs card" style="left:257px">
  <div class="pic" role="img" aria-label="White satin baby shoes"></div>
  <div class="name">Organza Trim Christening<br>Bootie WHITE</div>
  <svg class="stars" width="72" height="12"><g fill="#f6c20c"><use href="#star" x="0" width="12" height="12"/><use href="#star" x="15" width="12" height="12"/><use href="#star" x="30" width="12" height="12"/><use href="#star" x="45" width="12" height="12"/></g><use href="#star" x="60" width="12" height="12" fill="none" stroke="#f6c20c" stroke-width=".9"/></svg>
  <div class="price">$14.00</div><div class="btn">ADD TO CART</div>
</article>
<article class="abs card" style="left:457px">
  <div class="pic" role="img" aria-label="White christening bib with cross"></div>
  <div class="name">Organza Trim Christening<br>Bootie WHITE</div>
  <svg class="stars" width="72" height="12"><g fill="#f6c20c"><use href="#star" x="0" width="12" height="12"/><use href="#star" x="15" width="12" height="12"/><use href="#star" x="30" width="12" height="12"/><use href="#star" x="45" width="12" height="12"/></g><use href="#star" x="60" width="12" height="12" fill="none" stroke="#f6c20c" stroke-width=".9"/></svg>
  <div class="price">$14.00</div><div class="btn">ADD TO CART</div>
</article>
<article class="abs card" style="left:658px">
  <div class="pic" role="img" aria-label="White boys christening outfit with hat"></div>
  <div class="name">Organza Trim Christening<br>Bootie WHITE</div>
  <svg class="stars" width="72" height="12"><g fill="#f6c20c"><use href="#star" x="0" width="12" height="12"/><use href="#star" x="15" width="12" height="12"/><use href="#star" x="30" width="12" height="12"/><use href="#star" x="45" width="12" height="12"/></g><use href="#star" x="60" width="12" height="12" fill="none" stroke="#f6c20c" stroke-width=".9"/></svg>
  <div class="price">$14.00</div><div class="btn">ADD TO CART</div>
</article>

<section class="abs sale" role="img" aria-label="White baby booties on folded blue fabric">
  <svg class="abs sale-band" viewBox="0 0 781 89"><path d="M0 0H323L264 89H0z" fill="var(--teal-dark)"/></svg>
  <h2>SPRING SALE!</h2>
  <p>Upto 20% OFF</p>
  <div class="btn">SHOP NOW</div>
</section>

<section class="abs perks">
  <div class="perk" style="width:302px;padding-left:62px;gap:16px">
    <svg width="45" height="36" viewBox="0 0 45 36"><rect x="2" y="8" width="26" height="20" fill="#fff"/><path d="M29 14h9l6 7v7H29z" fill="#fff"/><circle cx="10" cy="31" r="4" fill="#fff" stroke="var(--teal-mid)" stroke-width="2"/><circle cx="36" cy="31" r="4" fill="#fff" stroke="var(--teal-mid)" stroke-width="2"/><path d="M15 23V12M10 16l5-5 5 5" stroke="var(--teal-mid)" stroke-width="2.5" fill="none"/></svg>
    <div><h4>FREE SHIPPING</h4><small>ON ORDERS $49 &amp; UP</small></div>
  </div>
  <div class="perk" style="width:288px;padding-left:36px;gap:20px;background:var(--teal-dark)">
    <svg width="50" height="50" viewBox="0 0 50 50"><path d="M2 8h8l8 26h22l5-17" stroke="#fff" stroke-width="3.5" fill="none"/><circle cx="20" cy="43" r="3.5" fill="#fff"/><circle cx="37" cy="43" r="3.5" fill="#fff"/><path d="M22 10a10 10 0 1 0 15 6" stroke="#fff" stroke-width="3" fill="none"/><path d="M19 6l4 5-6 2" stroke="#fff" stroke-width="3" fill="none"/></svg>
    <div><h4>EASY RETURNS</h4><small>FOR UP TO 60 DAYS</small></div>
  </div>
  <div class="perk" style="width:301px;padding-left:20px;gap:18px">
    <svg width="32" height="44" viewBox="0 0 32 44"><path d="M8 18V10a8 8 0 0 1 16 0v8" stroke="#fff" stroke-width="3.5" fill="none"/><rect x="2" y="18" width="28" height="24" fill="#fff"/><text x="6" y="37" font-size="14" font-weight="700" fill="var(--teal-mid)" font-family="Roboto,sans-serif">$</text><path d="M18 26h8M18 31h8M18 36h8" stroke="var(--teal-mid)" stroke-width="2"/></svg>
    <div><h4>SECURE SHOPPING</h4><small>SHOP WITH CONFIDENCE</small></div>
  </div>
</section>

<footer class="abs footer"></footer>
<div class="abs copy">Copyright ©2015.Company Name.All Right Reserved<br>Privacy Policy &nbsp;| &nbsp;Term Of Services</div>
<div class="abs social"><span class="lbl">Connect Us:</span>
  <i style="background:#3b5a9a"></i><i style="background:#2aa3e0"></i><i style="background:#333"></i><i style="background:#c92a3d"></i><i style="background:#d9452f"></i><i style="background:#c9272b"></i>
</div>
</body>
</html>
```